Business Card Design Project

We require a business card template to cover basic contact information - our company logo, names of employees, title, mobile and email.

Target Market(s)

Corporate

Industry/Entity Type

Business

Font styles to use
Sans Serif

Requirements
Nice to have
• Thinking it would be great just to have the logo taking up approximately half the space (so it goes as far across the top of the card as possible) and then contact details in the lower half of the card. Keen just to use only the two colours in the logo, on a white background.
Should not have
• No fussy drawings

```html
<!DOCTYPE html>
<html lang="en">
<head>
<meta charset="utf-8">
<title>Tidewell Developments – Business Card</title>
<link rel="stylesheet" href="https://fonts.googleapis.com/css2?family=Arimo:wght@400;700&display=swap">
<style>
  :root {
    --teal: #2fa3b5;
    --blue: #2f64ab;
    --card: #ffffff;
    --backdrop: #e9ebee;
  }
  * { margin: 0; padding: 0; box-sizing: border-box; }
  html, body {
    width: 1200px;
    height: 960px;
    overflow: hidden;
    background: var(--backdrop);
    font-family: "Arimo", Arial, sans-serif;
  }
  .business-card {
    position: absolute;
    left: 130px;
    top: 210px;
    width: 940px;
    height: 540px;
    background: var(--card);
    box-shadow: 0 6px 18px rgba(0, 0, 0, 0.18);
  }
  .company-name {
    position: absolute;
    left: 60px;
    top: 70px;
    font-size: 66px;
    font-weight: 400;
    color: var(--teal);
    letter-spacing: -1px;
    white-space: nowrap;
  }
  .contact-block {
    position: absolute;
    right: 70px;
    bottom: 70px;
    text-align: right;
  }
  .person-name {
    font-size: 38px;
    font-weight: 700;
    color: var(--blue);
    line-height: 1.2;
  }
  .person-title {
    font-size: 36px;
    color: var(--teal);
    line-height: 1.3;
    margin-bottom: 10px;
  }
  .contact-line {
    display: flex;
    align-items: center;
    justify-content: flex-end;
    gap: 16px;
    font-size: 34px;
    color: var(--blue);
    line-height: 1.4;
  }
  .contact-icon {
    flex: none;
    stroke: var(--teal);
    fill: none;
    stroke-width: 3;
  }
</style>
</head>
<body>
  <main class="business-card">
    <h1 class="company-name">Tidewell Developments</h1>

    <section class="contact-block">
      <p class="person-name">Alex Carter</p>
      <p class="person-title">Program Director</p>
      <p class="contact-line">
        <svg class="contact-icon" width="28" height="44" viewBox="0 0 28 44" aria-hidden="true">
          <rect x="3" y="2" width="22" height="40" rx="4"/>
          <line x1="11" y1="36" x2="17" y2="36"/>
        </svg>
        <span>555.555.0198 ext.214</span>
      </p>
      <p class="contact-line">
        <svg class="contact-icon" width="44" height="32" viewBox="0 0 44 32" aria-hidden="true">
          <rect x="2" y="2" width="40" height="28"/>
          <polyline points="2,2 22,18 42,2"/>
          <line x1="2" y1="30" x2="17" y2="14"/>
          <line x1="42" y1="30" x2="27" y2="14"/>
        </svg>
        <span>acarter@tidewell.com</span>
      </p>
    </section>
  </main>
</body>
</html>
```